Lundor Vapor Cleaning website for demos

Lundor Vapor Cleaning is a business that provides commercial cleaning services utilizing steam vapor, which offers the most effective and ecologically friendly method of cleaning today. We need a website to advertise our services, and needs to incorporate spaces to show video demonstrations on how the cleaning machine works.

Target Market(s)

The potential market for this business are hotels, motels, restaurants, hospitals, fast food facilities, nursing homes, day care centers, schools, country clubs, churches, office and apartment buildings, malls, movie theaters, super markets, airports, parks, and any other facility.

Industry/Entity Type

Business

Coding

Coded - Design and coding required

Number of Pages Required

3 page

Colors
add136
9bcb3c
34a6d7
3176b5
edf8f6

Requirements
Must have
• Areas for videos that serve as demonstrations of our services

```html
<!DOCTYPE html>
<html lang="en">
<head>
<meta charset="utf-8">
<title>Lundor Vapor Cleaning</title>
<link href="https://fonts.googleapis.com/css2?family=Michroma&family=Open+Sans:wght@400;600;700&display=swap" rel="stylesheet">
<style>
:root{
  --blue:#3a7cc4;
  --blue-dark:#3176b5;
  --blue-light:#34a6d7;
  --navy:#1e3f73;
  --ink:#333;
  --muted:#666;
  --rule:#d8d8d8;
  --footer:#16181c;
  --footer-bar:#0f1013;
  --white:#fff;
}
*{box-sizing:border-box;margin:0;padding:0}
html,body{width:682px;height:1200px;overflow:hidden;background:var(--white)}
body{font-family:"Open Sans",Arial,sans-serif;color:var(--ink);position:relative}
.abs{position:absolute}
.topline{left:0;top:0;width:682px;height:8px;background:var(--blue)}
.header{left:0;top:8px;width:682px;height:70px;background:linear-gradient(180deg,#f3f8fc,#fff)}
.brand{left:56px;top:24px;display:flex;align-items:center;gap:8px}
.brand-dot{width:30px;height:30px;border-radius:50%;background:var(--blue-dark)}
.brand-name{font-family:"Open Sans",sans-serif;font-weight:700;font-size:15px;color:var(--blue-dark);line-height:1.05}
.search{left:516px;top:31px;width:110px;height:24px;border:1px solid #c8c8c8;background:#fff;font-size:7px;color:#999;padding:7px 0 0 8px}
.search svg{position:absolute;right:7px;top:5px}
.nav{left:0;top:78px;width:682px;height:27px;background:var(--blue);display:flex}
.nav a{font-family:"Michroma",sans-serif;font-size:7.5px;color:var(--white);text-decoration:none;display:flex;align-items:center;justify-content:center;height:27px;border-right:1px solid rgba(255,255,255,.4)}
.nav a:last-child{border-right:0}
.nav a.current{color:var(--navy)}
.hero{left:0;top:105px;width:682px;height:265px;background:linear-gradient(180deg,#6f9ccc 0%,#a9c4df 45%,#dbe6ef 100%)}
.hero-title{left:0;top:48px;width:682px;text-align:center;font-family:"Michroma",sans-serif;font-size:27px;line-height:43px;color:rgba(214,226,240,.9)}
.hero-title .strong{color:rgba(38,78,150,.85)}
.arrow{top:110px;width:18px;height:18px}
.features{left:0;top:370px;width:682px;height:177px;background:var(--blue)}
.feature{top:17px;width:142px;color:var(--white)}
.feature h3{font-weight:700;font-size:11.5px;line-height:13px;height:40px;letter-spacing:.2px}
.feature p{font-size:7.2px;line-height:11.7px;color:#e6eef8}
.btn{display:inline-block;background:var(--blue-light);color:var(--white);font-size:6.8px;font-weight:600;text-align:center;border-bottom:2px solid #2a8ab8;text-decoration:none}
.feature .btn{position:absolute;top:121px;left:0;width:68px;height:25px;line-height:23px}
.sec-title{font-family:"Michroma",sans-serif;font-size:11.5px;color:#2d2d2d;letter-spacing:.5px}
.welcome-text{left:56px;top:612px;width:354px;font-size:7.2px;line-height:13.2px;color:#555}
.news-item{left:440px;width:190px}
.news-item h4{font-size:9px;font-weight:600;color:var(--blue-dark)}
.news-item p{font-size:7px;line-height:10px;color:#555;margin-top:5px}
.meta{display:flex;gap:12px;font-size:6.8px;color:#777;margin-top:5px}
.link{font-size:7.5px;font-weight:600;color:var(--blue-dark);text-decoration:underline}
.divider{left:56px;top:761px;width:350px;height:1px;background:var(--rule)}
.vdivider{left:209px;top:790px;width:1px;height:168px;background:var(--rule)}
.checklist{left:56px;top:819px;list-style:none}
.checklist li{font-size:7px;color:#444;height:20px;display:flex;align-items:center;gap:6px}
.thumb{width:81px;height:63px;border:1px solid #999;border-radius:2px}
.video{left:440px;top:819px;width:185px;height:177px;background:var(--blue)}
.controls{position:absolute;left:0;bottom:0;width:185px;height:15px;background:#1b2432;display:flex;align-items:center;gap:4px;padding:0 5px;font-size:5px;color:#ccc}
.footer{left:0;top:1027px;width:682px;height:139px;background:radial-gradient(ellipse at 50% 0%,#2a2d33,var(--footer) 70%)}
.footer h5{font-size:9.5px;font-weight:600;color:var(--white);letter-spacing:.3px}
.footer .logo-text{font-family:"Michroma",sans-serif;font-size:9.5px;color:var(--blue-light);line-height:14px}
.footer p{font-size:7px;line-height:11px;color:#ddd}
.social{list-style:none}
.social li{display:flex;align-items:center;gap:10px;height:20px;font-size:7px;color:var(--blue-light)}
.social span.sq{width:9px;height:9px;background:#ddd}
.fcol-rule{top:1040px;width:1px;height:100px;background:#2c2f35}
.footer-bar{left:0;top:1166px;width:682px;height:34px;background:var(--footer-bar);text-align:center;font-size:7px;color:#999;line-height:34px}
</style>
</head>
<body>
<div class="abs topline"></div>
<header class="abs header"></header>
<div class="abs brand"><span class="brand-dot"></span><span class="brand-name">Lundor Vapor<br>Cleaning</span></div>
<div class="abs search">SEARCH
  <svg width="14" height="14" viewBox="0 0 14 14"><circle cx="5.5" cy="5.5" r="4" fill="none" stroke="#aaa" stroke-width="1.6"/><line x1="8.5" y1="8.5" x2="13" y2="13" stroke="#aaa" stroke-width="2"/></svg>
</div>
<nav class="abs nav">
  <a class="current" style="width:120px">HOME</a>
  <a style="width:102px">ABOUT US</a>
  <a style="width:90px">NEWS »</a>
  <a style="width:135px">WHY CHOOSE US</a>
  <a style="width:101px">SERVICES</a>
  <a style="width:134px">CONTACT</a>
</nav>

<section class="abs hero" role="img" aria-label="Photo of a woman leaping across a cloudy sky holding a steam vacuum cleaner">
  <div class="abs hero-title">COMMERCIAL<br>CLEANING<br><span class="strong">UTILIZING STEAM</span><br>VAPOUR</div>
  <svg class="abs arrow" style="left:17px" viewBox="0 0 18 18"><circle cx="9" cy="9" r="8" fill="#cfe0f0" stroke="#2c5f9e" stroke-width="1.4"/><path d="M11.5 5 5.5 9l6 4-1.5-4z" fill="#2c5f9e"/></svg>
  <svg class="abs arrow" style="left:640px" viewBox="0 0 18 18"><circle cx="9" cy="9" r="8" fill="#cfe0f0" stroke="#2c5f9e" stroke-width="1.4"/><path d="M6.5 5l6 4-6 4 1.5-4z" fill="#2c5f9e"/></svg>
</section>

<section class="abs features">
  <div class="abs feature" style="left:56px"><h3>NO CHEMICALS OR SOAPS</h3><p>Lorem Ipsum is simply dummy text of the printing and typesetting industry. Lorem Ipsum has been the industry's standard dummy text ever since the 1500s, when an unknown printer took a galley.</p><a class="btn">READ MORE</a></div>
  <div class="abs feature" style="left:202px"><h3>SAFE &amp; ECO-FRIENDLY GREEN CLEANING</h3><p>Lorem Ipsum is simply dummy text of the printing and typesetting industry. Lorem Ipsum has been the industry's standard dummy text ever since the 1500s, when an unknown printer took a galley.</p><a class="btn">READ MORE</a></div>
  <div class="abs feature" style="left:348px"><h3>CLEANS, SANITIZES, DEODORIZES</h3><p>Lorem Ipsum is simply dummy text of the printing and typesetting industry. Lorem Ipsum has been the industry's standard dummy text ever since the 1500s, when an unknown printer took a galley.</p><a class="btn">READ MORE</a></div>
  <div class="abs feature" style="left:497px"><h3>CAUSES NO ALLERGIES</h3><p>Lorem Ipsum is simply dummy text of the printing and typesetting industry. Lorem Ipsum has been the industry's standard dummy text ever since the 1500s, when an unknown printer took a galley.</p><a class="btn">READ MORE</a></div>
</section>

<h2 class="abs sec-title" style="left:56px;top:581px">WELCOME</h2>
<p class="abs welcome-text">This is an eco-friendly process that employs hot steam vapor to effectively clean andsterilize. Steam can penetrate pores and clean more thoroughly without commercial chemical cleaners, whereas hot steam destroys mold as well as spores, germs, viruses, dust mites, and bacteria leaving the surface clean and sanitized.Steam Vapor cleaning cuts grease, sanitizes, kills mold, mildew, bacteria and other allergy causing pathogens. Vapor cleaning uses no chemicals which eliminates one of the largest costs of cleaning services, the chemicals.</p>
<a class="abs btn" style="left:56px;top:703px;width:74px;height:25px;line-height:23px">READ MORE</a>

<h2 class="abs sec-title" style="left:438px;top:581px">OUR NEWS</h2>
<article class="abs news-item" style="top:614px">
  <h4>LOREM IPSUM DOLOR SIT AMET</h4>
  <p>Aliquam dapibus tincidunt metus. Praesent justo dolor, lobortis quis, lobortis .</p>
  <div class="meta"><span>▦ February 14, 2013</span><span>● admin</span><span>▰ 2 Comments</span></div>
</article>
<article class="abs news-item" style="top:677px">
  <h4>LOREM IPSUM DOLOR SIT AMET</h4>
  <p>Aliquam dapibus tincidunt metus. Praesent justo dolor, lobortis quis, lobortis.</p>
  <div class="meta"><span>▦ February 14, 2013</span><span>● admin</span><span>▰ 2 Comments</span></div>
</article>
<a class="abs link" style="left:440px;top:738px">SEE MORE</a>

<div class="abs divider"></div>

<h2 class="abs sec-title" style="left:56px;top:786px">WHY CHOOSE US</h2>
<div class="abs vdivider"></div>
<ul class="abs checklist">
  <li><svg width="7" height="7" viewBox="0 0 7 7"><path d="M0 2.5h3.5V0L7 3.5 3.5 7V4.5H0z" fill="#3176b5"/></svg>Quickly, easily removes dirt, stains &amp;</li>
  <li><svg width="7" height="7" viewBox="0 0 7 7"><path d="M0 2.5h3.5V0L7 3.5 3.5 7V4.5H0z" fill="#3176b5"/></svg>Reduce water &amp; chemical consumption</li>
  <li><svg width="7" height="7" viewBox="0 0 7 7"><path d="M0 2.5h3.5V0L7 3.5 3.5 7V4.5H0z" fill="#3176b5"/></svg>Clean hard to reach nooks &amp; crannies</li>
  <li><svg width="7" height="7" viewBox="0 0 7 7"><path d="M0 2.5h3.5V0L7 3.5 3.5 7V4.5H0z" fill="#3176b5"/></svg>Eliminate waste-water &amp; overspray</li>
  <li><svg width="7" height="7" viewBox="0 0 7 7"><path d="M0 2.5h3.5V0L7 3.5 3.5 7V4.5H0z" fill="#3176b5"/></svg>Two operators can clean at once</li>
  <li><svg width="7" height="7" viewBox="0 0 7 7"><path d="M0 2.5h3.5V0L7 3.5 3.5 7V4.5H0z" fill="#3176b5"/></svg>Deodorize &amp; sterilize surfaces</li>
  <li><svg width="7" height="7" viewBox="0 0 7 7"><path d="M0 2.5h3.5V0L7 3.5 3.5 7V4.5H0z" fill="#3176b5"/></svg>Easy to maintain &amp; operate</li>
</ul>
<a class="abs link" style="left:56px;top:975px">READ MORE</a>

<h2 class="abs sec-title" style="left:225px;top:786px">RECENT PROJECTS</h2>
<div class="abs thumb" style="left:224px;top:818px;background:linear-gradient(135deg,#7ccb3a,#bfe07a)" role="img" aria-label="Photo of a cleaner holding a feather duster"></div>
<div class="abs thumb" style="left:325px;top:818px;background:linear-gradient(180deg,#8d8d8d,#555)" role="img" aria-label="Photo of a worker pressure-washing a street"></div>
<div class="abs thumb" style="left:224px;top:896px;background:linear-gradient(135deg,#e8e8e8,#bcd4e4)" role="img" aria-label="Photo of a cleaner wiping a window"></div>
<div class="abs thumb" style="left:325px;top:896px;background:linear-gradient(135deg,#3a6fc4,#e3c23a 60%,#d43a2a)" role="img" aria-label="Photo of a cleaning crew with equipment"></div>
<a class="abs link" style="left:227px;top:975px">SEE MORE</a>

<h2 class="abs sec-title" style="left:440px;top:786px">FEATURE VIDEO</h2>
<div class="abs video" role="img" aria-label="Demonstration video of the steam cleaning machine">
  <svg style="position:absolute;left:78px;top:76px" width="30" height="30" viewBox="0 0 30 30"><circle cx="15" cy="15" r="14" fill="#1b2432" stroke="#dfe8f2" stroke-width="1.5"/><path d="M11 9l11 6-11 6z" fill="#fff"/></svg>
  <div class="controls"><span>▶</span><span>❚❚</span><span>■</span><span style="flex:1;height:2px;background:#fff;margin:0 4px"></span><span>1.08/12.06</span><span>◀)</span></div>
</div>

<footer class="abs footer"></footer>
<div class="abs" style="left:56px;top:1043px;width:150px">
  <div class="logo-text">LUNDOR VAPOR<br>CLEANING</div>
  <p style="font-size:7px;line-height:11px;color:#ddd;margin-top:8px">Sed ut perspiciatis unde omnis iste natus error sit voluptatem accusantium doloremque laudantium, totam rem aperiam, eaque ipsa quae ab illo inventore veritatis et quasi.</p>
</div>
<div class="abs fcol-rule" style="left:238px"></div>
<div class="abs" style="left:294px;top:1044px">
  <h5 style="font-size:9.5px;font-weight:600;color:#fff">FOLLOW US</h5>
  <ul class="social" style="margin-top:6px">
    <li><span class="sq"></span>Friendsite</li>
    <li><span class="sq"></span>Chirper</li>
    <li><span class="sq"></span>Circles</li>
  </ul>
</div>
<div class="abs fcol-rule" style="left:395px"></div>
<div class="abs" style="left:440px;top:1044px;width:200px">
  <h5 style="font-size:9.5px;font-weight:600;color:#fff">CONTACT US</h5>
  <p style="font-size:7px;line-height:11px;color:#ddd;margin-top:9px">The name and address of the business is:<br>Lundor Vapor Cleaning<br>212 Harbor Mill Rd. Suite 14<br>Westbrook, ME 04092<br>Website: <span style="color:#34a6d7">lundorvapor.com</span></p>
</div>
<div class="abs footer-bar">© 2015 Lundor Vapor Cleaning. All Rights Reserved.</div>
</body>
</html>
```